"Lantern Field" Play - Poster Design for Theatre Group

We are an amateur theatre group based in Geneva, Switzerland. We take pride in eye-catching posters for our shows, which are printed in various sizes.
This design will be for a play in March 2016. The play is called "Lantern Field", and it's a Harwick Medal winner from Morgan Pellew-Strand. The play is about a couple who have everything a family could want, until they lose a child in a life-shattering accident that turns their world upside down. The play charts the couple's bittersweet search to find each other and to find comfort.
Most importantly, we want a design that will make people want to see the show. We don't want to give away the plot or be too heavy-handed about death, but we want it to be clear that it's not a comedy (although there are some lighter moments!).
Attached you will find a template for the poster. This simply has our group name and logo in the top right corner: (Lakeside Stage Players Circle presents).
You may change the color of both the text and the logo, but please do not change the font, size, or location.
Here is the information that needs to be on the poster, wherever you see fit:
play title: Lantern Field
author byline: by Morgan Pellew-Strand
director line: directed by Ned Variscombe
tagline: How do you keep it together when your whole world's fallen apart?
dates and times:
1-5 March 2016
(Tue-Fri 20:00, Sat 19:00)
location:
Théâtre du Vieux Moulin
Eaux-Vives, Geneva
websites:
www.lspc.ch
www.scenesauboulevard.ch
Technical Details:
Any font or combination of fonts is acceptable. The largest text should be the play title. The author's name must be at least 50% of the title font size.
For this competition, we would like the version with A3 proportions, which will also be used at F4 (89.5 x 128 cm) and A5 sizes (14.8 x 21 cm). Therefore no text should be below 9pt at A5.
However, from the winning designer we will also need repurposed sizes of the same design. Here is a comprehensive list of the sizes we will need.
1) A3 print poster. Artwork should be 300dpi, CMYK, sent with a 1mm bleed all round, to specification PDF/X-1A:2001. We will need this image in PDF format in addition to the default Artmarketly formats.
2) Friendora advert picture. 1200px by 628px, RGB jpeg. This must comply with Friendora’s restrictions on amount of text, which is no more than 20% of area taken up by text.(https://www.friendora.example/ads/tools/text_overlay).
Because of these restrictions it is sufficient to include just the title and the author's name in this version.
3) Friendora cover picture: 851px by 314px. RGB jpeg. It is sufficient to include just the title and the author's name in this version.
4) Web banner. 1000px by 300px. RGB jpeg. This version should include just the main image(s), no text.

```html
<!DOCTYPE html>
<html lang="en">
<head>
<meta charset="utf-8">
<title>Lantern Field – Poster</title>
<link rel="stylesheet" href="https://fonts.googleapis.com/css2?family=Roboto+Condensed:wght@400;700;900&family=Kalam:wght@700&family=Arimo:wght@400&display=swap">
<style>
  :root {
    --ink-dark: #0d0c0b;
    --stone-warm: #8a8576;
    --stone-cool: #6d7079;
    --glow: #f4f1e6;
    --title-grey: #e4e4e4;
    --logo-grey: #d9d9d9;
    --white: #ffffff;
    --director-red: #c3262b;
    --tagline-ink: #111111;
  }
  * { margin: 0; padding: 0; box-sizing: border-box; }
  html, body { width: 865px; height: 1200px; overflow: hidden; background: var(--ink-dark); }
  .poster {
    position: relative;
    width: 865px;
    height: 1200px;
    overflow: hidden;
    font-family: "Roboto Condensed", "Arial Narrow", sans-serif;
  }
  .stairwell-photo {
    position: absolute;
    inset: 0;
    background:
      radial-gradient(circle at 420px 695px, var(--glow) 0 115px, rgba(230,228,215,0.6) 140px, rgba(0,0,0,0) 210px),
      radial-gradient(ellipse 380px 480px at 420px 690px, rgba(0,0,0,0) 55%, rgba(13,12,11,0.85) 100%),
      linear-gradient(90deg, #2a2720 0%, var(--stone-warm) 28%, #a9a592 48%, var(--stone-cool) 49%, #4a4c55 75%, #161618 100%);
  }
  .stairwell-photo::after {
    content: "";
    position: absolute;
    inset: 0;
    background:
      linear-gradient(180deg, rgba(0,0,0,0) 0 900px, rgba(13,12,11,0.55) 1030px, rgba(13,12,11,0.7) 1200px),
      radial-gradient(ellipse 520px 640px at 430px 660px, rgba(0,0,0,0) 55%, var(--ink-dark) 100%);
  }
  .presenter {
    position: absolute;
    top: 70px;
    right: 168px;
    text-align: right;
    color: var(--logo-grey);
    font-weight: 700;
    font-size: 17px;
    line-height: 22px;
  }
  .presenter-mark {
    position: absolute;
    top: 45px;
    left: 718px;
    width: 92px;
    height: 92px;
    border-radius: 50%;
    background: var(--logo-grey);
  }
  .title-arc {
    position: absolute;
    inset: 0;
    width: 865px;
    height: 1200px;
  }
  .title-arc text {
    font-family: "Roboto Condensed", "Arial Narrow", sans-serif;
    font-weight: 900;
    font-size: 104px;
    fill: var(--title-grey);
  }
  .tagline {
    position: absolute;
    top: 426px;
    left: 332px;
    width: 205px;
    text-align: center;
    font-family: "Kalam", cursive;
    font-weight: 700;
    font-size: 17px;
    line-height: 25px;
    color: var(--tagline-ink);
  }
  .credits {
    position: absolute;
    top: 1022px;
    left: 145px;
    display: flex;
    align-items: baseline;
    gap: 12px;
    white-space: nowrap;
  }
  .byline { color: var(--white); font-weight: 700; font-size: 39px; }
  .director-label { color: var(--ink-dark); font-weight: 700; font-size: 13px; }
  .director-name { color: var(--director-red); font-weight: 700; font-size: 29px; }
  .details {
    position: absolute;
    top: 1072px;
    left: 0;
    width: 865px;
    text-align: center;
    font-family: "Arimo", Arial, sans-serif;
    color: var(--white);
    font-size: 19px;
    line-height: 26px;
  }
  .details p:nth-child(2) { padding-left: 40px; }
</style>
</head>
<body>
  <main class="poster">
    <div class="stairwell-photo" role="img" aria-label="Photograph looking up a spiral stone staircase toward a bright round window, left half warm-toned, right half cool-toned"></div>

    <div class="presenter">Lakeside Stage<br>Players Circle<br>presents</div>
    <div class="presenter-mark" aria-hidden="true"></div>

    <svg class="title-arc" viewBox="0 0 865 1200" aria-labelledby="play-title">
      <title id="play-title">Lantern Field</title>
      <defs>
        <path id="title-curve" d="M 92 420 Q 390 200 700 475"/>
      </defs>
      <text>
        <textPath href="#title-curve" textLength="650" lengthAdjust="spacingAndGlyphs">Lantern Field</textPath>
      </text>
    </svg>

    <p class="tagline">How do you keep it together when your whole world's fallen apart?</p>

    <div class="credits">
      <span class="byline">by Morgan Pellew-Strand</span>
      <span class="director-label">directed by</span>
      <span class="director-name">Ned Variscombe</span>
    </div>

    <div class="details">
      <p>1-5 March 2016 (Tue-Fri 20:00, Sat 19:00)</p>
      <p>Théâtre du Vieux Moulin, Eaux-Vives, Geneva www.lspc.ch</p>
      <p>www.scenesauboulevard.ch</p>
    </div>
  </main>
</body>
</html>
```